Fiber Arts Workshop: Business Cards & Stationery
Copper Kettle StitchHouse, LLC
Fiber Arts Workshop: Business Cards & Stationery - Hobbies
Creative Brief
Bright & Fun-filled
Marla Penrose
Principal
48 Birchwood Terrace #512 Millbrook, New Jersey 07322
marla.penrose@ckstitchhouse.example
www.ckstitchhouse.example
Fonts - you may use fonts other than those used in the logo if they enhance the design

```html
<!DOCTYPE html>
<html lang="en">
<head>
<meta charset="utf-8">
<title>Copper Kettle StitchHouse – Business Cards</title>
<link rel="stylesheet" href="https://fonts.googleapis.com/css2?family=Questrial&family=Open+Sans:wght@400;600&display=swap">
<style>
  :root {
    --backdrop: #ece8e3;
    --card-white: #fbfbfa;
    --ink: #4d4d4d;
    --ink-soft: #6a6a6a;
    --divider: #c9c9c9;
    --plum: #8b2a6b;
    --tangerine: #ee5a2c;
    --violet: #7b4a9e;
    --amber: #d98330;
  }
  * { box-sizing: border-box; margin: 0; padding: 0; }
  html, body {
    width: 1200px; height: 720px; overflow: hidden;
    background: var(--backdrop);
  }
  .card-sheet {
    width: 1200px; height: 720px;
    display: grid;
    grid-template-columns: 562px 562px;
    grid-template-rows: 330px 330px;
    gap: 30px 36px;
    padding: 22px 20px;
  }
  .card {
    position: relative;
    background: var(--accent);
    padding: 18px;
    box-shadow: 0 3px 10px rgba(0,0,0,.25);
  }
  .card--plum { --accent: var(--plum); }
  .card--tangerine { --accent: var(--tangerine); }
  .card--violet { --accent: var(--violet); }
  .card--amber { --accent: var(--amber); }
  .card__face {
    position: relative;
    width: 100%; height: 100%;
    background: var(--card-white);
    overflow: hidden;
  }
  .card__flourish {
    position: absolute;
    right: -40px; top: 60px;
    width: 300px; height: 260px;
    background: radial-gradient(ellipse at 60% 55%, color-mix(in srgb, var(--accent) 22%, transparent), transparent 70%);
  }
  .brand {
    position: absolute; left: 48px; top: 54px;
    display: flex; align-items: center; gap: 18px;
  }
  .brand__dot {
    width: 74px; height: 74px; border-radius: 50%;
    background: var(--accent);
  }
  .brand__name {
    font-family: 'Questrial', sans-serif;
    font-size: 31px; line-height: 1.12;
    color: var(--ink);
  }
  .person {
    position: absolute; right: 274px; top: 196px;
    text-align: right;
    font-family: 'Open Sans', sans-serif;
    font-size: 11.5px; line-height: 1.45;
    color: var(--accent);
  }
  .contact {
    position: absolute; left: 262px; top: 190px;
    padding-left: 12px;
    border-left: 1px solid var(--divider);
    list-style: none;
    font-family: 'Open Sans', sans-serif;
    font-size: 11px; line-height: 1.4;
    color: var(--ink-soft);
    white-space: nowrap;
  }
  .contact__item {
    display: flex; gap: 7px; align-items: flex-start;
    margin-bottom: 3px;
  }
  .contact__icon {
    flex: none; width: 13px; height: 13px; margin-top: 1px;
  }
  .contact__icon circle { fill: var(--accent); }
  .contact__icon path { fill: none; stroke: #fff; stroke-width: 1.3; stroke-linecap: round; stroke-linejoin: round; }
</style>
</head>
<body>
<main class="card-sheet">

  <article class="card card--plum">
    <div class="card__face">
      <div class="brand"><span class="brand__dot"></span><p class="brand__name">Copper Kettle<br>StitchHouse</p></div>
      <p class="person">Marla Penrose<br>Principal</p>
      <ul class="contact">
        <li class="contact__item"><svg class="contact__icon" viewBox="0 0 14 14"><circle cx="7" cy="7" r="7"/><path d="M7 11 C4.5 8 4.5 6.5 4.5 6 a2.5 2.5 0 0 1 5 0 c0 .5 0 2-2.5 5z"/></svg><span>48 Birchwood Terrace #512<br>Millbrook, New Jersey 07322</span></li>
        <li class="contact__item"><svg class="contact__icon" viewBox="0 0 14 14"><circle cx="7" cy="7" r="7"/><path d="M4.5 4 l1.5-.3 1 2-1 .8 a5 5 0 0 0 2.5 2.5 l.8-1 2 1-.3 1.5 C7 10.5 3.5 7 4.5 4z"/></svg><span>(973) 555-0187</span></li>
        <li class="contact__item"><svg class="contact__icon" viewBox="0 0 14 14"><circle cx="7" cy="7" r="7"/><path d="M3.8 4.8 h6.4 v4.4 h-6.4z M3.8 4.8 L7 7.3 10.2 4.8"/></svg><span>marla.penrose@ckstitchhouse.example</span></li>
      </ul>
    </div>
  </article>

  <article class="card card--tangerine">
    <div class="card__face">
      <div class="card__flourish" role="img" aria-label="Faint flowing yarn strands decoration"></div>
      <div class="brand"><span class="brand__dot"></span><p class="brand__name">Copper Kettle<br>StitchHouse</p></div>
      <p class="person">Marla Penrose<br>Principal</p>
      <ul class="contact">
        <li class="contact__item"><svg class="contact__icon" viewBox="0 0 14 14"><circle cx="7" cy="7" r="7"/><path d="M7 11 C4.5 8 4.5 6.5 4.5 6 a2.5 2.5 0 0 1 5 0 c0 .5 0 2-2.5 5z"/></svg><span>48 Birchwood Terrace #512<br>Millbrook, New Jersey 07322</span></li>
        <li class="contact__item"><svg class="contact__icon" viewBox="0 0 14 14"><circle cx="7" cy="7" r="7"/><path d="M4.5 4 l1.5-.3 1 2-1 .8 a5 5 0 0 0 2.5 2.5 l.8-1 2 1-.3 1.5 C7 10.5 3.5 7 4.5 4z"/></svg><span>(973) 555-0187</span></li>
        <li class="contact__item"><svg class="contact__icon" viewBox="0 0 14 14"><circle cx="7" cy="7" r="7"/><path d="M3.8 4.8 h6.4 v4.4 h-6.4z M3.8 4.8 L7 7.3 10.2 4.8"/></svg><span>marla.penrose@ckstitchhouse.example</span></li>
      </ul>
    </div>
  </article>

  <article class="card card--violet">
    <div class="card__face">
      <div class="card__flourish" role="img" aria-label="Faint flowing yarn strands decoration"></div>
      <div class="brand"><span class="brand__dot"></span><p class="brand__name">Copper Kettle<br>StitchHouse</p></div>
      <p class="person">Marla Penrose<br>Principal</p>
      <ul class="contact">
        <li class="contact__item"><svg class="contact__icon" viewBox="0 0 14 14"><circle cx="7" cy="7" r="7"/><path d="M7 11 C4.5 8 4.5 6.5 4.5 6 a2.5 2.5 0 0 1 5 0 c0 .5 0 2-2.5 5z"/></svg><span>48 Birchwood Terrace #512<br>Millbrook, New Jersey 07322</span></li>
        <li class="contact__item"><svg class="contact__icon" viewBox="0 0 14 14"><circle cx="7" cy="7" r="7"/><path d="M4.5 4 l1.5-.3 1 2-1 .8 a5 5 0 0 0 2.5 2.5 l.8-1 2 1-.3 1.5 C7 10.5 3.5 7 4.5 4z"/></svg><span>(973) 555-0187</span></li>
        <li class="contact__item"><svg class="contact__icon" viewBox="0 0 14 14"><circle cx="7" cy="7" r="7"/><path d="M3.8 4.8 h6.4 v4.4 h-6.4z M3.8 4.8 L7 7.3 10.2 4.8"/></svg><span>marla.penrose@ckstitchhouse.example</span></li>
      </ul>
    </div>
  </article>

  <article class="card card--amber">
    <div class="card__face">
      <div class="card__flourish" role="img" aria-label="Faint flowing yarn strands decoration"></div>
      <div class="brand"><span class="brand__dot"></span><p class="brand__name">Copper Kettle<br>StitchHouse</p></div>
      <p class="person">Marla Penrose<br>Principal</p>
      <ul class="contact">
        <li class="contact__item"><svg class="contact__icon" viewBox="0 0 14 14"><circle cx="7" cy="7" r="7"/><path d="M7 11 C4.5 8 4.5 6.5 4.5 6 a2.5 2.5 0 0 1 5 0 c0 .5 0 2-2.5 5z"/></svg><span>48 Birchwood Terrace #512<br>Millbrook, New Jersey 07322</span></li>
        <li class="contact__item"><svg class="contact__icon" viewBox="0 0 14 14"><circle cx="7" cy="7" r="7"/><path d="M4.5 4 l1.5-.3 1 2-1 .8 a5 5 0 0 0 2.5 2.5 l.8-1 2 1-.3 1.5 C7 10.5 3.5 7 4.5 4z"/></svg><span>(973) 555-0187</span></li>
        <li class="contact__item"><svg class="contact__icon" viewBox="0 0 14 14"><circle cx="7" cy="7" r="7"/><path d="M3.8 4.8 h6.4 v4.4 h-6.4z M3.8 4.8 L7 7.3 10.2 4.8"/></svg><span>marla.penrose@ckstitchhouse.example</span></li>
      </ul>
    </div>
  </article>

</main>
</body>
</html>
```